Need help in designing new business card utilizing our new logo.

BuildMarq Solutions works with Construction Business Owners, Managers & IT Professionals to strengthen software usage and increase user productivity.

Our Construction Accounting and Mobile Field Management Software Clients engage with us in the following areas:

New Software Implementations
Software Re-Implementations
Redesigning Software Usage at the User Level
Project Coordination & Management
Continued Software Support

Old tag line:
Weighing Options - Implementing Solutions

www.buildmarq-solutions.example

Stride 4 is a product, but not needed for a new business card.

```html
<!DOCTYPE html>
<html lang="en">
<head>
<meta charset="utf-8">
<title>BuildMarq Solutions – Business Card</title>
<link rel="stylesheet" href="https://fonts.googleapis.com/css2?family=Montserrat:wght@600&family=Questrial&family=Open+Sans:wght@400&display=swap">
<style>
  :root {
    --brand-blue: #233a95;
    --brand-grey: #c1c1c3;
    --ink: #2b2b2b;
    --paper: #ffffff;
  }
  * { margin: 0; padding: 0; box-sizing: border-box; }
  html, body { width: 1200px; height: 1200px; overflow: hidden; background: var(--paper); }
  .canvas { position: relative; width: 1200px; height: 1200px; }
  .card-shapes { position: absolute; left: 0; top: 0; width: 1200px; height: 1200px; }

  .wordmark { position: absolute; display: flex; align-items: center; gap: 10px; }
  .wordmark__square { background: var(--brand-blue); flex: none; }
  .wordmark__name {
    font-family: "Montserrat", sans-serif; font-weight: 600; color: var(--brand-blue);
    line-height: 1; letter-spacing: -0.5px;
  }
  .wordmark__sub {
    font-family: "Montserrat", sans-serif; font-weight: 600; color: var(--brand-grey);
    line-height: 1;
  }

  .front-mark { left: 74px; top: 478px; }
  .front-mark .wordmark__square { width: 60px; height: 60px; }
  .front-mark .wordmark__text { border-left: 2px solid var(--brand-blue); padding-left: 6px; }
  .front-mark .wordmark__name { font-size: 36px; }
  .front-mark .wordmark__sub { font-size: 16px; letter-spacing: 16.5px; margin-top: 6px; }

  .services { position: absolute; left: 28px; top: 568px; list-style: none;
    font-family: "Questrial", sans-serif; font-size: 15.5px; color: var(--ink); letter-spacing: 0.8px; }
  .services li { height: 21.6px; display: flex; align-items: center; gap: 8px; }
  .services svg { width: 10px; height: 10px; flex: none; }

  .contact { position: absolute; left: 24px; top: 712px; font-family: "Open Sans", sans-serif;
    font-size: 8.2px; color: #333; letter-spacing: 0.4px; }
  .contact__row { display: flex; align-items: center; gap: 6px; margin-bottom: 5px; line-height: 10px; }
  .contact__icon { width: 16px; height: 14px; flex: none; }
  .contact__icon--square { width: 8px; height: 8px; margin: 0 4px; background: var(--brand-blue); }

  .phone { position: absolute; left: 295px; top: 740px; display: flex; align-items: center; gap: 4px;
    font-family: "Open Sans", sans-serif; font-size: 22px; color: #111; }
  .phone svg { width: 26px; height: 26px; }

  .back-mark { position: absolute; left: 740px; top: 512px; width: 270px; text-align: center; }
  .back-mark .wordmark__square { width: 100px; height: 100px; margin: 0 auto 26px; }
  .back-mark .wordmark__name { font-size: 40px; }
  .back-mark .wordmark__sub { font-size: 18px; letter-spacing: 15px; margin-top: 8px; padding-left: 15px; }
  .back-mark .website { font-family: "Questrial", sans-serif; font-size: 14px; color: var(--brand-blue);
    letter-spacing: 1.4px; margin-top: 6px; }
</style>
</head>
<body>
<main class="canvas">
  <svg class="card-shapes" viewBox="0 0 1200 1200" aria-hidden="true">
    <!-- front card bands -->
    <polygon points="0,792 0,705 470,729" fill="var(--brand-grey)"/>
    <polygon points="0,701 425,701 425,528 578,444 578,490 472,550 470,729 0,705" fill="var(--brand-blue)"/>
    <!-- back card chevrons -->
    <polygon points="956,444 1030,444 993,482" fill="var(--brand-blue)"/>
    <polygon points="1054,444 1128,444 993,580 993,504" fill="var(--brand-grey)"/>
    <polygon points="1146,444 1200,444 1200,506 1104,598 1200,690 1200,792 1166,792 994,598" fill="var(--brand-blue)"/>
    <polygon points="1200,528 1126,600 1200,676" fill="var(--brand-grey)"/>
  </svg>

  <div class="wordmark front-mark">
    <span class="wordmark__square"></span>
    <div class="wordmark__text">
      <div class="wordmark__name">BUILDMARQ</div>
      <div class="wordmark__sub">SOLUTIONS</div>
    </div>
  </div>

  <ul class="services">
    <li><svg viewBox="0 0 10 10"><path d="M1 5 L4 8 L9 2" stroke="var(--brand-blue)" stroke-width="2" fill="none"/></svg>New Software Implementations</li>
    <li><svg viewBox="0 0 10 10"><path d="M1 5 L4 8 L9 2" stroke="var(--brand-blue)" stroke-width="2" fill="none"/></svg>Software Re-Implementations</li>
    <li><svg viewBox="0 0 10 10"><path d="M1 5 L4 8 L9 2" stroke="var(--brand-blue)" stroke-width="2" fill="none"/></svg>Redesigning Software Usage at the User Level</li>
    <li><svg viewBox="0 0 10 10"><path d="M1 5 L4 8 L9 2" stroke="var(--brand-blue)" stroke-width="2" fill="none"/></svg>Project Coordination &amp; Management</li>
    <li><svg viewBox="0 0 10 10"><path d="M1 5 L4 8 L9 2" stroke="var(--brand-blue)" stroke-width="2" fill="none"/></svg>Continued Software Support</li>
  </ul>

  <div class="contact">
    <div class="contact__row">
      <svg class="contact__icon" viewBox="0 0 16 14"><path d="M8 0 L16 7 L13.5 7 L13.5 14 L10 14 L10 9 L6 9 L6 14 L2.5 14 L2.5 7 L0 7 Z" fill="var(--brand-blue)"/></svg>
      <span>48B Harbor Lane - PMB 107<br>Lakeview Falls, NY 12000</span>
    </div>
    <div class="contact__row">
      <svg class="contact__icon" viewBox="0 0 16 14"><rect x="1" y="3" width="14" height="9" fill="none" stroke="var(--brand-blue)" stroke-width="1.4"/><path d="M1 3 L8 9 L15 3" fill="none" stroke="var(--brand-blue)" stroke-width="1.4"/></svg>
      <span>Mail: info@buildmarq-solutions.example</span>
    </div>
    <div class="contact__row">
      <span class="contact__icon contact__icon--square"></span>
      <span>Social: BuildMarq Solutions, LLC</span>
    </div>
  </div>

  <div class="phone">
    <svg viewBox="0 0 26 26"><circle cx="13" cy="13" r="11.5" fill="none" stroke="var(--brand-blue)" stroke-width="2"/><path d="M8.5 7.5 l2.5 -0.5 1.5 3 -1.5 1.2 q1 2.5 3.5 3.8 l1.3 -1.4 3 1.6 -0.6 2.5 q-6 0.5 -9.7 -10.2 z" fill="var(--brand-blue)"/></svg>
    <span>866-555-0142</span>
  </div>

  <div class="wordmark back-mark" style="display:block">
    <div class="wordmark__square"></div>
    <div class="wordmark__name">BUILDMARQ</div>
    <div class="wordmark__sub">SOLUTIONS</div>
    <div class="website">www.buildmarq-solutions.example</div>
  </div>
</main>
</body>
</html>
```